Healthcare and Professional IT Services Company need a redesigned business card

We are a IT Services company that targets small medical practices and professional business such as Attorneys, Accounts, Architects etc. We want to communicate a professional yet friendly image using recent logo redesign here on Sketchforge. Like to see the colors blue and orange in the design. Must use the Copper Lantern Technology as displayed in the new logo - then also want to incorporate the fish logo as well.

Target Market(s)

Small medical and professional services

Industry/Entity Type

It Company

Contact Information for Business Card

The usual stuff, place for name address phone website. Also maybe our tagline which is "Guided by technology"

Requirements
Must have
• My new logo and the fish somewhere on the card

```html
<!DOCTYPE html>
<html lang="en">
<head>
<meta charset="utf-8">
<title>Copper Lantern Technology – Business Card</title>
<link rel="stylesheet" href="https://fonts.googleapis.com/css2?family=Montserrat:wght@600;700&family=Open+Sans:wght@400;600&display=swap">
<style>
  :root {
    --brand-blue: #1596dc;
    --brand-blue-deep: #0f86cc;
    --accent-orange: #f7a23b;
    --ink-grey: #4a4a4a;
    --paper: #ffffff;
    --backdrop: #e9ecef;
  }
  * { margin: 0; padding: 0; box-sizing: border-box; }
  html, body { width: 1200px; height: 750px; overflow: hidden; }
  body {
    background: var(--backdrop);
    display: flex;
    align-items: center;
    justify-content: center;
    gap: 48px;
    font-family: "Open Sans", Arial, sans-serif;
  }
  .card {
    width: 525px;
    height: 300px;
    position: relative;
    overflow: hidden;
    box-shadow: 0 6px 18px rgba(0,0,0,0.12);
  }
  /* Front */
  .card-front {
    background: var(--brand-blue);
    color: var(--paper);
    display: flex;
    flex-direction: column;
    align-items: center;
    justify-content: center;
    gap: 22px;
  }
  .brand-lockup {
    display: flex;
    align-items: center;
    gap: 14px;
  }
  .brand-dot {
    width: 26px; height: 26px; border-radius: 50%;
    background: currentColor;
    flex: none;
  }
  .brand-name {
    font-family: "Montserrat", Arial, sans-serif;
    font-weight: 700;
    font-size: 30px;
    line-height: 1.05;
    letter-spacing: 0.2px;
  }
  .card-front .brand-name { color: var(--paper); }
  .tagline {
    font-family: "Montserrat", Arial, sans-serif;
    font-weight: 600;
    font-size: 15px;
    letter-spacing: 0.3px;
  }
  /* Back */
  .card-back { background: var(--paper); }
  .edge-marker {
    position: absolute;
    left: -22px; top: 118px;
    width: 44px; height: 44px;
    border-radius: 50%;
    background: var(--brand-blue-deep);
  }
  .contact-block {
    position: absolute;
    left: 44px; top: 70px;
  }
  .person-name {
    font-family: "Montserrat", Arial, sans-serif;
    font-weight: 600;
    font-size: 19px;
    color: var(--brand-blue);
  }
  .person-title {
    font-size: 14px;
    color: var(--accent-orange);
    margin-top: 2px;
  }
  .address {
    font-size: 13px;
    line-height: 1.5;
    color: var(--ink-grey);
    margin: 16px 0 0 22px;
  }
  .contact-list {
    list-style: none;
    margin: 16px 0 0 22px;
    font-size: 13px;
    color: var(--ink-grey);
  }
  .contact-list li {
    display: flex; align-items: center; gap: 10px;
    line-height: 1.65;
  }
  .contact-list svg { width: 14px; height: 14px; fill: var(--brand-blue); flex: none; }
  .card-back .brand-lockup {
    position: absolute;
    right: 36px; top: 90px;
    color: var(--brand-blue);
  }
  .card-back .brand-name { font-size: 26px; color: var(--brand-blue); }
</style>
</head>
<body>
  <section class="card card-front" aria-label="Card front">
    <div class="brand-lockup">
      <span class="brand-dot"></span>
      <span class="brand-name">Copper Lantern<br>Technology</span>
    </div>
    <p class="tagline">Guided by technology</p>
  </section>

  <section class="card card-back" aria-label="Card back">
    <span class="edge-marker"></span>
    <div class="contact-block">
      <h1 class="person-name">Martin Vale</h1>
      <p class="person-title">President</p>
      <p class="address">2417 Harborview Lane<br>Elm Ridge<br>NY 10952</p>
      <ul class="contact-list">
        <li>
          <svg viewBox="0 0 24 24" aria-hidden="true"><path d="M6.6 10.8a15.2 15.2 0 0 0 6.6 6.6l2.2-2.2c.3-.3.7-.4 1-.2 1.1.4 2.3.6 3.6.6.6 0 1 .4 1 1V20c0 .6-.4 1-1 1A17 17 0 0 1 3 4c0-.6.4-1 1-1h3.5c.6 0 1 .4 1 1 0 1.3.2 2.5.6 3.6.1.3 0 .7-.2 1z"/></svg>
          555 0192 4486
        </li>
        <li>
          <svg viewBox="0 0 24 24" aria-hidden="true"><path d="M2 5h20v14H2V5zm2 2v.3l8 6 8-6V7H4z"/></svg>
          martin@copperlantern.example
        </li>
        <li>
          <svg viewBox="0 0 24 24" aria-hidden="true"><path d="M12 2a10 10 0 1 0 0 20 10 10 0 0 0 0-20zm6.9 6h-3a15 15 0 0 0-1.3-3.9A8 8 0 0 1 18.9 8zM12 4c.8 1.2 1.5 2.5 1.9 4h-3.8c.4-1.5 1.1-2.8 1.9-4zM4.3 14a8 8 0 0 1 0-4h3.4a16 16 0 0 0 0 4H4.3zm.8 2h3a15 15 0 0 0 1.3 3.9A8 8 0 0 1 5.1 16zm3-8h-3a8 8 0 0 1 4.3-3.9A15 15 0 0 0 8.1 8zM12 20c-.8-1.2-1.5-2.5-1.9-4h3.8c-.4 1.5-1.1 2.8-1.9 4zm2.3-6H9.7a14 14 0 0 1 0-4h4.6a14 14 0 0 1 0 4zm.3 5.9a15 15 0 0 0 1.3-3.9h3a8 8 0 0 1-4.3 3.9zm1.7-5.9a16 16 0 0 0 0-4h3.4a8 8 0 0 1 0 4h-3.4z"/></svg>
          www.copperlantern.example
        </li>
      </ul>
    </div>
    <div class="brand-lockup">
      <span class="brand-dot"></span>
      <span class="brand-name">Copper Lantern<br>Technology</span>
    </div>
  </section>
</body>
</html>
```